Tavo Payments Business card refresh

Need a new design of our business card The info is not what is on these cards i sent this for a reference. I can email all the info over
Info would be Derek Whitfield Chief TAVO is the title. our new address is 47615 Birch Hollow Rd. Westlake Village Ca 91384 Cell number is 805-634-2917 Work number is 855-482-7309 ext 212 Derek@tavopayments.com is my email address
Target Market(s)
Merchant Services all businesses that take credit cards
Industry/Entity Type
Merchant Services / Credit Card processing
Contact Information for Business Card
Need a new design of our business card The info is not what is on these cards i sent this for a reference. I can email all the info over Info would be Derek Whitfield Chief TAVO is the title. our new address is 47615 Birch Hollow Rd. Westlake Village Ca 91384 Cell number is 805-634-2917 Work number is 855-482-7309 ext 212 Derek@tavopayments.com is my email address
Requirements
Must have
- My logo and colors from my brand guidelines
Nice to have
- i sent some designs just need a new refresh
Should not have
- nothing specific

```html
<!DOCTYPE html>
<html lang="en">
<head>
<meta charset="utf-8">
<title>Tavo Payments Business Card</title>
<link href="https://fonts.googleapis.com/css2?family=Poppins:wght@400;500;600;700;800&display=swap" rel="stylesheet">
<style>
  :root {
    --page: #ececec;
    --ink: #111111;
    --slate: #262d33;
    --black: #0b0c0d;
    --green: #8cc63f;
    --white: #ffffff;
    --faint: #e9e9ea;
  }
  * { margin: 0; padding: 0; box-sizing: border-box; }
  html, body { width: 1200px; height: 1165px; overflow: hidden; }
  body {
    background: var(--page);
    font-family: "Poppins", sans-serif;
    position: relative;
  }
  .card {
    position: absolute;
    top: 425px;
    width: 520px;
    height: 314px;
    overflow: hidden;
    box-shadow: 0 6px 18px rgba(0,0,0,0.12);
  }
  .card-front { left: 60px; background: var(--white); }
  .card-back { left: 620px; background: var(--slate); }
  .front-shape { position: absolute; inset: 0; }

  .wordmark {
    position: absolute;
    left: 40px;
    top: 92px;
    color: var(--white);
    font-weight: 600;
    font-size: 52px;
    line-height: 1;
    letter-spacing: 1px;
  }
  .wordmark-sub {
    position: absolute;
    left: 42px;
    top: 162px;
    color: var(--green);
    font-weight: 500;
    font-size: 14px;
    letter-spacing: 6px;
  }
  .address {
    position: absolute;
    left: 42px;
    top: 204px;
    color: var(--white);
    font-weight: 500;
    font-size: 11px;
    line-height: 1.35;
  }
  .faint-name {
    position: absolute;
    right: 20px;
    bottom: -14px;
    color: var(--faint);
    font-weight: 800;
    font-size: 74px;
    line-height: 1;
  }
  .holder-name {
    position: absolute;
    left: 253px;
    top: 36px;
    color: var(--ink);
    font-weight: 800;
    font-size: 22px;
    letter-spacing: 2px;
  }
  .holder-title {
    position: absolute;
    left: 253px;
    top: 72px;
    color: var(--green);
    font-weight: 600;
    font-size: 17px;
    letter-spacing: 2px;
  }
  .contact-list {
    position: absolute;
    left: 280px;
    top: 118px;
    list-style: none;
  }
  .contact-list li {
    display: flex;
    align-items: center;
    height: 38px;
    font-weight: 600;
    font-size: 13px;
    color: var(--ink);
  }
  .contact-icon {
    width: 24px;
    height: 24px;
    margin-right: 12px;
    flex: none;
  }

  .services {
    position: absolute;
    left: 60px;
    top: 62px;
    list-style: none;
    color: var(--white);
    font-weight: 500;
    font-size: 11px;
    line-height: 1.25;
  }
  .referral {
    position: absolute;
    left: 60px;
    top: 230px;
    color: var(--green);
    font-weight: 500;
    font-size: 11px;
    line-height: 1.25;
  }
  .back-name {
    position: absolute;
    right: 26px;
    bottom: 26px;
    color: var(--green);
    font-weight: 800;
    font-size: 64px;
    line-height: 1;
  }
</style>
</head>
<body>

<section class="card card-front" aria-label="Business card front">
  <svg class="front-shape" viewBox="0 0 520 314" width="520" height="314" aria-hidden="true">
    <path d="M0 0 H158 C258 10 228 170 300 250 C330 285 360 300 392 314 H0 Z" fill="var(--black)"/>
    <path d="M0 0 H142 C238 8 206 160 262 240 C280 268 300 292 330 314 H0 Z" fill="var(--slate)"/>
  </svg>
  <div class="faint-name" aria-hidden="true">TAVO</div>
  <div class="wordmark">TAVO</div>
  <div class="wordmark-sub">PAYMENTS</div>
  <address class="address">47615 Birch Hollow Rd.<br>Westlake Village<br>Ca 91384</address>

  <h1 class="holder-name">DEREK WHITFIELD</h1>
  <p class="holder-title">CHIEF TAVO</p>
  <ul class="contact-list">
    <li>
      <svg class="contact-icon" viewBox="0 0 24 24" aria-hidden="true"><circle cx="12" cy="12" r="12" fill="var(--green)"/><path d="M8.2 6.5l2 2.3-1.2 1.5c.8 1.7 2 2.9 3.7 3.7l1.5-1.2 2.3 2-1.1 1.9c-4.3-.6-7.6-3.9-8.2-8.2z" fill="var(--ink)"/></svg>
      805-634-2917
    </li>
    <li>
      <svg class="contact-icon" viewBox="0 0 24 24" aria-hidden="true"><circle cx="12" cy="12" r="12" fill="var(--green)"/><path d="M8.2 6.5l2 2.3-1.2 1.5c.8 1.7 2 2.9 3.7 3.7l1.5-1.2 2.3 2-1.1 1.9c-4.3-.6-7.6-3.9-8.2-8.2z" fill="var(--ink)"/></svg>
      855-482-7309
    </li>
    <li>
      <svg class="contact-icon" viewBox="0 0 24 24" aria-hidden="true"><circle cx="12" cy="12" r="12" fill="var(--green)"/><rect x="6.5" y="8" width="11" height="8" rx="1" fill="var(--ink)"/><path d="M6.8 8.5l5.2 4 5.2-4" stroke="var(--green)" stroke-width="1.1" fill="none"/></svg>
      Derek@tavopayments.com
    </li>
  </ul>
</section>

<section class="card card-back" aria-label="Business card back">
  <ul class="services">
    <li>Credit Card Processing</li>
    <li>Check Guarantee</li>
    <li>Gift Cards</li>
    <li>Loyalty Cards</li>
    <li>ACH Deposits</li>
    <li>24/7 Customer Support</li>
    <li>Same Day Approvals</li>
    <li>ATM Sales</li>
    <li>ATM Placement</li>
    <li>Merchant Funding</li>
  </ul>
  <p class="referral">Ask about our<br>"Merchant Referral" Program</p>
  <div class="back-name">TAVO</div>
</section>

</body>
</html>
```